HVAC Parts Distributor Website

We are working with an HVAC parts distributor to design a website. They primarily work with HVAC contractors.
They are similar to: https://www.brakenfieldparts.com, and https://www.ventorbin.com
Thank you for taking the time to consider designing a website for us. We are web developers based in Stockton, CA, USA. Most of our projects go through the same process. Understanding this process may help you win a project with us. We custom-code all of our websites in-house. We don’t have any requirements as to what tools you use for your design, but we ask that you follow these guidelines.
IMAGES:
If you use any images or icons in the design, we ask that you have a link to the asset so we can purchase the image/icon. Most of the designs we submit do not have the customer’s images on them unless they have some great images. Be creative; show us the feeling you are trying to portray with your image choices. Use any royalty-free site you choose. We subscribe to Veltrix and mainly use their images, but we can purchase images outside of Veltrix.
FONTS:
We ask that you identify the fonts you’re using in the design. This can be done in a message if you want. We typically use Quillon Fonts and Veltrix Fonts.
CONTENT:
We're always open to different content and ideas. We often submit designs with stock images so the client can see our vision. We typically take pictures after the website launch to use their images with our vision. Lorem Ipsum is fine for paragraphs, but we ask that you make the Headers with correct English. We want to be able to show the vision and identify the sections of the website.
INSPIRATION:
We typically add a couple of links in the brief of websites we like to help you get started in your design.
REVISIONS:
We do not often ask for revisions of the designs unless we see something in the design that may not appeal to the client. If there are slight changes that we want to make, we simply do that in the development process.
FEEDBACK:
We rarely give feedback on designs during the design process. We are working on many website projects and do not have the time to give feedback. We usually respond if your request is well thought out and asks specific questions, but a note asking “feedback, please” usually goes unanswered.
1 page

```html
<!DOCTYPE html>
<html lang="en">
<head>
<meta charset="utf-8">
<title>Kestral HVAC Distribution</title>
<link href="https://fonts.googleapis.com/css2?family=Josefin+Sans:wght@400;600&family=Poppins:wght@600;800&display=swap" rel="stylesheet">
<style>
:root{
  --green:#8ea30e;
  --green-dark:#6f8209;
  --ink:#2d2a2e;
  --text:#222;
  --muted:#7a7a7a;
  --pale:#eef1f5;
  --circle:#e2e4e8;
  --white:#fff;
}
*{box-sizing:border-box;margin:0;padding:0}
html,body{width:1200px;height:2905px;overflow:hidden}
body{font-family:"Josefin Sans",sans-serif;color:var(--text);background:var(--white);position:relative}
.abs{position:absolute}
.h{font-family:"Poppins",sans-serif;font-weight:800;text-transform:uppercase;letter-spacing:-.5px}
.h .accent{color:var(--green)}
.btn{display:inline-flex;align-items:center;justify-content:center;background:var(--green);color:#fff;border-radius:20px;font-size:12px;text-transform:uppercase;letter-spacing:.5px;box-shadow:0 3px 0 var(--green-dark)}
.round{border-radius:50%;background:var(--green);display:flex;align-items:center;justify-content:center}

/* header */
.site-header{top:0;left:0;width:1200px;height:75px}
.brand{left:120px;top:16px;font-family:"Poppins",sans-serif;font-weight:800;font-size:30px;color:var(--ink);line-height:1;display:flex;align-items:center;gap:8px}
.brand-mark{width:14px;height:14px;background:var(--green)}
.brand small{display:block;font-family:"Josefin Sans",sans-serif;font-weight:600;font-size:13px;letter-spacing:1px;color:var(--ink)}
.search{left:504px;top:23px;width:282px;height:37px;border:1px solid #ddd;border-radius:20px;font-size:11px;color:var(--muted);padding:13px 0 0 22px}
.search .round{position:absolute;right:3px;top:3px;width:30px;height:30px}
.tools-btn{left:803px;top:23px;width:169px;height:37px}
.icon-btn{top:22px;width:40px;height:40px}
.cart-count{position:absolute;top:-4px;right:-2px;width:13px;height:13px;border-radius:50%;background:#fff;color:var(--green);font-size:8px;display:flex;align-items:center;justify-content:center;border:1px solid var(--green)}

.main-nav{top:75px;left:0;width:1200px;height:36px;background:var(--ink);display:flex;padding-left:120px}
.main-nav a{color:#fff;text-decoration:none;font-size:10.5px;font-weight:600;padding:13px 12px 0;text-transform:uppercase}
.main-nav a.active{background:var(--green)}

/* hero */
.hero{top:111px;left:0;width:1200px;height:512px;background:linear-gradient(100deg,#4a4b4f 0%,#6d6a66 35%,#8a2a28 62%,#5a4a40 85%,#3e4a2c 100%)}
.hero-shade{inset:0;background:linear-gradient(90deg,rgba(20,20,20,.55),rgba(20,20,20,.1) 65%)}
.hero h1{left:120px;top:154px;font-size:39px;line-height:44px;color:#fff;letter-spacing:0}
.hero p{left:120px;top:250px;color:#fff;font-size:19px;line-height:23px;letter-spacing:.4px}
.hero .btn{left:120px;top:315px;width:119px;height:34px}

/* categories */
.categories{top:623px;left:0;width:1200px;height:249px;background:var(--pale)}
.cat{top:0;width:195px;height:249px;text-align:center}
.cat .disc{width:107px;height:107px;border-radius:50%;background:var(--circle);margin:30px auto 0;display:flex;align-items:center;justify-content:center}
.cat .label{font-size:19px;margin-top:17px}
.cat .go{margin-top:18px;color:var(--green);font-size:16px}
.cat.active{background:var(--green);width:179px}
.cat.active .disc{background:#fff}
.cat.active .label{color:#fff}
.cat.active .go{width:38px;height:38px;border-radius:50%;background:#fff;margin:14px auto 0;display:flex;align-items:center;justify-content:center}
.slide-arrow{width:38px;height:38px;box-shadow:0 2px 0 var(--green-dark)}

/* about */
.about-shadow{left:154px;top:985px;width:435px;height:332px;background:var(--ink)}
.about-bar{left:154px;top:1280px;width:435px;height:37px;background:var(--green)}
.about-photo{left:120px;top:948px;width:434px;height:332px;background:linear-gradient(135deg,#cfd3d6,#8f959a 45%,#3f5a86 80%,#3a3d48)}
.about h2{left:635px;top:955px;font-size:37px}
.about .copy{left:656px;top:1013px;width:420px;font-size:11.4px;line-height:18px}
.about .copy p+p{margin-top:18px}
.about .btn{left:635px;top:1263px;width:117px;height:36px}

/* subscribe */
.subscribe{top:1393px;left:0;width:1200px;height:201px;background:linear-gradient(110deg,#90a617,#7e9510 60%,#8aa115)}
.subscribe h2{left:120px;top:64px;font-size:37px;color:#fff}
.subscribe h2 .accent{color:var(--ink)}
.subscribe p{left:120px;top:116px;color:#fff;font-size:12px}
.sub-form{left:611px;top:79px;width:469px;height:44px;background:#f2f3ea;border-radius:22px;border:2px solid #fff;font-size:10.5px;color:var(--muted);padding:16px 0 0 20px}
.sub-form .btn{position:absolute;right:2px;top:2px;width:104px;height:36px;box-shadow:none}

/* reviews */
.reviews h2{left:0;width:1200px;text-align:center;top:1660px;font-size:37px}
.quote-mark{left:570px;top:1725px;width:60px;height:60px;border-radius:50%;background:var(--circle);font-family:"Poppins",sans-serif;font-size:30px;font-weight:600;display:flex;align-items:center;justify-content:center;color:var(--ink)}
.review-text{left:216px;top:1800px;width:768px;text-align:center;font-style:italic;color:var(--muted);font-size:14.5px;line-height:22.5px}
.reviewer{left:0;width:1200px;top:1962px;text-align:center;color:var(--green);font-size:18px}
.reviewer-from{left:0;width:1200px;top:1990px;text-align:center;font-size:10px;letter-spacing:.5px}
.dots{left:569px;top:2028px;display:flex;gap:9px}
.dots span{width:14px;height:14px;border-radius:50%;border:1px solid var(--green)}
.dots span.on{background:radial-gradient(circle,var(--green) 3px,transparent 3.5px)}

/* brands */
.brands{top:2117px;left:0;width:1200px;height:150px;background:var(--pale)}
.brand-tile{top:37px;width:178px;height:75px;background:#fff;border:1px solid #ddd;display:flex;align-items:center;justify-content:center;font-family:"Poppins",sans-serif;font-weight:600;font-size:22px;color:#555}

/* perks */
.perks h2{left:0;width:1200px;text-align:center;top:2333px;font-size:37px}
.perks .lead{left:0;width:1200px;text-align:center;top:2390px;font-size:13px}
.perk{top:2436px;width:180px;text-align:center}
.perk svg{display:block;margin:0 auto}
.perk h3{font-weight:400;font-size:15.5px;margin-top:16px}
.perk p{font-size:11px;color:var(--muted);line-height:17px;margin-top:6px}

/* footer */
.site-footer{top:2625px;left:0;width:1200px;height:280px;background:var(--ink);color:#fff}
.foot-col{top:45px}
.foot-col h4{font-family:"Poppins",sans-serif;font-weight:800;font-size:15px;text-transform:uppercase}
.foot-col h4 .accent{color:var(--green)}
.foot-col ul{list-style:none;margin-top:9px}
.foot-col li{font-size:12px;line-height:22.6px;display:flex;align-items:center;gap:8px}
.badge{left:855px;width:188px;background:#fff;border-radius:2px}
.badge .shape{position:absolute;left:50%;top:50%;transform:translate(-50%,-50%);border-radius:4px}
.foot-bottom{left:120px;top:230px;width:958px;border-top:1px solid #4a4650;padding-top:18px;font-size:10px;display:flex;align-items:center}
.foot-bottom .accent{color:var(--green)}
.social{display:flex;gap:8px;margin-left:44px}
.social span{width:36px;height:36px;border-radius:50%;background:var(--green);box-shadow:0 2px 0 var(--green-dark);display:flex;align-items:center;justify-content:center}
.social span i{width:10px;height:10px;border-radius:50%;background:#fff;display:block}
</style>
</head>
<body>

<header class="site-header abs">
  <div class="brand abs"><span class="brand-mark"></span><div>KESTRAL<small>HVAC DISTRIBUTION</small></div></div>
  <div class="search abs">Search For Products...
    <span class="round"><svg width="13" height="13" viewBox="0 0 14 14" fill="none" stroke="#fff" stroke-width="1.6"><circle cx="6" cy="6" r="4.5"/><path d="M9.5 9.5 13 13"/></svg></span>
  </div>
  <a class="btn tools-btn abs">Contractor Tools</a>
  <span class="round icon-btn abs" style="left:987px"><svg width="16" height="16" viewBox="0 0 16 16" fill="none" stroke="#fff" stroke-width="1.4"><circle cx="8" cy="5" r="3"/><path d="M2 15c0-3.5 2.7-5.5 6-5.5s6 2 6 5.5"/></svg></span>
  <span class="round icon-btn abs" style="left:1039px"><svg width="17" height="16" viewBox="0 0 18 16" fill="none" stroke="#fff" stroke-width="1.4"><path d="M1 1h3l2 9h9l2-7H5"/><circle cx="7" cy="14" r="1.3"/><circle cx="14" cy="14" r="1.3"/></svg><span class="cart-count">0</span></span>
</header>

<nav class="main-nav abs">
  <a class="active">HVAC Equipment</a><a>HVACR Parts</a><a>Hydronics &amp; Plumbing</a><a>Motors</a><a>Refrigeration</a><a>Supplies</a><a>Testing, Tools &amp; Training</a><a>Thermostats</a><a>Ventilation &amp; IAQ</a>
</nav>

<section class="hero abs" role="img" aria-label="HVAC technician in red work clothes servicing an outdoor heat pump unit">
  <div class="hero-shade abs"></div>
  <h1 class="h abs">We Equip HVAC<br>Professionals To Succeed.</h1>
  <p class="abs">The Leading Supplier of Heating, Air Conditioning,<br>and Plumbing Equipment.</p>
  <a class="btn abs">Contact Us</a>
</section>

<section class="categories abs">
  <span class="round slide-arrow abs" style="left:69px;top:106px"><svg width="12" height="12" viewBox="0 0 12 12" fill="none" stroke="#fff" stroke-width="1.5"><path d="M8 1 3 6l5 5"/></svg></span>
  <div class="cat abs" style="left:112px"><div class="disc"><svg width="52" height="52" viewBox="0 0 52 52" fill="none" stroke="#8ea30e" stroke-width="2"><path d="M6 20h16v8H6zM22 24h14v-8h10v28H36V32H22"/><path d="M14 8c-3 4-4 6-4 8a4 4 0 0 0 8 0c0-2-1-4-4-8z"/></svg></div><div class="label">Plumbing</div><div class="go">→</div></div>
  <div class="cat abs" style="left:307px"><div class="disc"><svg width="52" height="52" viewBox="0 0 52 52" fill="none" stroke="#8ea30e" stroke-width="2"><rect x="6" y="12" width="40" height="28" rx="2"/><circle cx="20" cy="26" r="8"/><path d="M34 18h8M34 23h8M34 28h8M34 33h8"/></svg></div><div class="label">HVAC</div><div class="go">→</div></div>
  <div class="cat active abs" style="left:510px"><div class="disc"><svg width="52" height="52" viewBox="0 0 52 52" fill="none" stroke="#8ea30e" stroke-width="2"><path d="M4 28h10v10H4zM38 28h10v10H38zM14 26h24v14H14z"/><path d="M26 26v-10M18 12h16"/></svg></div><div class="label">Valves</div><div class="go"><svg width="14" height="10" viewBox="0 0 14 10" fill="none" stroke="#8ea30e" stroke-width="1.5"><path d="M1 5h12M9 1l4 4-4 4"/></svg></div></div>
  <div class="cat abs" style="left:697px"><div class="disc"><svg width="52" height="52" viewBox="0 0 52 52" fill="none" stroke="#8ea30e" stroke-width="2"><rect x="8" y="26" width="36" height="16"/><path d="M16 26V10M24 26V14M32 26V8M40 26V16"/></svg></div><div class="label">Tools</div><div class="go">→</div></div>
  <div class="cat abs" style="left:892px"><div class="disc"><svg width="52" height="52" viewBox="0 0 52 52" fill="none" stroke="#8ea30e" stroke-width="2"><rect x="10" y="8" width="22" height="36"/><path d="M14 14h14v10H14zM23 28l-4 6h5l-3 6M32 24h6v-8M36 10v6M42 10v6"/></svg></div><div class="label">Electrical</div><div class="go">→</div></div>
  <span class="round slide-arrow abs" style="left:1094px;top:106px"><svg width="12" height="12" viewBox="0 0 12 12" fill="none" stroke="#fff" stroke-width="1.5"><path d="m4 1 5 5-5 5"/></svg></span>
</section>

<section class="about">
  <div class="about-shadow abs"></div>
  <div class="about-bar abs"></div>
  <div class="about-photo abs" role="img" aria-label="Technicians repairing an air conditioning condenser unit"></div>
  <h2 class="h abs">About <span class="accent">Kestral</span></h2>
  <div class="copy abs">
    <p>Lorem Ipsum is simply dummy text of the printing and typesetting industry. Lorem Ipsum has been the industry's standard dummy text ever since the 1500s, when an unknown printer took a galley of type and scrambled it to make a type specimen book. It has survived not only five centuries, but also the leap into electronic typesetting, remaining essentially unchanged. It was popularised in the 1960s with the release of Letraset sheets containing Lorem Ipsum passages, and more recently with desktop publishing software like Aldus PageMaker including versions of Lorem Ipsum.</p>
    <p>Lorem Ipsum is simply dummy text of the printing and typesetting industry. Lorem Ipsum has been the industry's standard dummy text ever since the 1500s, when an unknown printer took a galley of type and scrambled it to make a type specimen book.</p>
  </div>
  <a class="btn abs">About Us</a>
</section>

<section class="subscribe abs">
  <h2 class="h abs">Subscribe <span class="accent">For More</span></h2>
  <p class="abs">Stay in the know with top brands &amp; product spotlights!</p>
  <div class="sub-form abs">Your Email Address<a class="btn">Sign Up</a></div>
</section>

<section class="reviews">
  <h2 class="h abs">Customer <span class="accent">Reviews</span></h2>
  <div class="quote-mark abs">66</div>
  <span class="round slide-arrow abs" style="left:143px;top:1845px"><svg width="12" height="12" viewBox="0 0 12 12" fill="none" stroke="#fff" stroke-width="1.5"><path d="M8 1 3 6l5 5"/></svg></span>
  <p class="review-text abs">Lorem Ipsum is simply dummy text of the printing and typesetting industry. Lorem Ipsum has been the industry's standard dummy text ever since the 1500s, when an unknown printer took a galley of type and scrambled it to make a type specimen book. It has survived not only five centuries, but also the leap into electronic typesetting, remaining essentially unchanged. It was popularised in the 1960s with the release of Letraset sheets containing Lorem Ipsum passages, and more recently with desktop publishing software like Aldus PageMaker including versions of Lorem Ipsum.</p>
  <span class="round slide-arrow abs" style="left:1019px;top:1845px"><svg width="12" height="12" viewBox="0 0 12 12" fill="none" stroke="#fff" stroke-width="1.5"><path d="m4 1 5 5-5 5"/></svg></span>
  <div class="reviewer abs">Carla M</div>
  <div class="reviewer-from abs">FROM DALTON, GA</div>
  <div class="dots abs"><span></span><span class="on"></span><span></span></div>
</section>

<section class="brands abs">
  <div class="brand-tile abs" style="left:121px">Norwake</div>
  <div class="brand-tile abs" style="left:316px">Davlen</div>
  <div class="brand-tile abs" style="left:511px">Corrand</div>
  <div class="brand-tile abs" style="left:705px">Tessmark</div>
  <div class="brand-tile abs" style="left:899px">Ridgeforth</div>
</section>

<section class="perks">
  <h2 class="h abs">Being A <span class="accent">Pro Has Its</span> Perks!</h2>
  <p class="lead abs">Free Shipping. Free Gear. Free Membership.</p>
  <div class="perk abs" style="left:120px"><svg width="52" height="46" viewBox="0 0 52 46" fill="none" stroke="#2d2a2e" stroke-width="1.8"><rect x="3" y="8" width="30" height="26"/><path d="M33 16h9l7 9v9H33"/><circle cx="13" cy="38" r="4"/><circle cx="40" cy="38" r="4"/><path d="M8 18h6M8 24h4"/></svg><h3>Free Shipping</h3><p>Your shipping costs are always on the house</p></div>
  <div class="perk abs" style="left:315px"><svg width="52" height="46" viewBox="0 0 52 46" fill="none" stroke="#2d2a2e" stroke-width="1.8"><path d="M12 4v22H5l21 18 21-18h-7V4"/><path d="M22 12h8M22 18h8M26 8v16"/></svg><h3>Lower Prices</h3><p>Competitive advantage with discounts on every order</p></div>
  <div class="perk abs" style="left:510px"><svg width="52" height="46" viewBox="0 0 52 46" fill="none" stroke="#2d2a2e" stroke-width="1.8"><circle cx="26" cy="23" r="20"/><path d="M16 17l10-5 10 5v12l-10 5-10-5zM16 17l10 5 10-5M26 22v12"/></svg><h3>Free Returns</h3><p>We cover all return costs and fees</p></div>
  <div class="perk abs" style="left:705px"><svg width="52" height="46" viewBox="0 0 52 46" fill="none" stroke="#2d2a2e" stroke-width="1.8"><circle cx="26" cy="23" r="15"/><path d="M26 2v6M26 38v6M5 23h6M41 23h6M19 19h14l-7 11z"/></svg><h3>Exclusive Gear</h3><p>Get free TradePro merchandise with select orders</p></div>
  <div class="perk abs" style="left:900px"><svg width="52" height="46" viewBox="0 0 52 46" fill="none" stroke="#2d2a2e" stroke-width="1.8"><path d="M10 6l7 8-4 5c3 6 7 10 13 13l5-4 8 7-5 6C20 40 6 26 5 11z"/><path d="M32 6c4 1 7 4 8 8M32 12c2 .5 3 2 3.5 3.5"/></svg><h3>Dedicated Phone Line</h3><p>Receive fast and friendly support exclusively for pros</p></div>
</section>

<footer class="site-footer abs">
  <div class="foot-col abs" style="left:120px"><h4>Quick <span class="accent">Links</span></h4>
    <ul><li><svg width="10" height="10" viewBox="0 0 10 10" fill="none" stroke="#8ea30e"><circle cx="5" cy="5" r="4.3"/><path d="m3 5 1.5 1.5L7 4"/></svg>Home</li><li><svg width="10" height="10" viewBox="0 0 10 10" fill="none" stroke="#8ea30e"><circle cx="5" cy="5" r="4.3"/><path d="m3 5 1.5 1.5L7 4"/></svg>Meet The Team</li><li><svg width="10" height="10" viewBox="0 0 10 10" fill="none" stroke="#8ea30e"><circle cx="5" cy="5" r="4.3"/><path d="m3 5 1.5 1.5L7 4"/></svg>Careers</li><li><svg width="10" height="10" viewBox="0 0 10 10" fill="none" stroke="#8ea30e"><circle cx="5" cy="5" r="4.3"/><path d="m3 5 1.5 1.5L7 4"/></svg>Our Blog</li><li><svg width="10" height="10" viewBox="0 0 10 10" fill="none" stroke="#8ea30e"><circle cx="5" cy="5" r="4.3"/><path d="m3 5 1.5 1.5L7 4"/></svg>Contact Us</li></ul></div>
  <div class="foot-col abs" style="left:365px"><h4>Resources &amp; <span class="accent">Tools</span></h4>
    <ul><li><svg width="10" height="10" viewBox="0 0 10 10" fill="none" stroke="#8ea30e"><circle cx="5" cy="5" r="4.3"/><path d="m3 5 1.5 1.5L7 4"/></svg>Reorder</li><li><svg width="10" height="10" viewBox="0 0 10 10" fill="none" stroke="#8ea30e"><circle cx="5" cy="5" r="4.3"/><path d="m3 5 1.5 1.5L7 4"/></svg>Quick Order</li><li><svg width="10" height="10" viewBox="0 0 10 10" fill="none" stroke="#8ea30e"><circle cx="5" cy="5" r="4.3"/><path d="m3 5 1.5 1.5L7 4"/></svg>Saved Carts</li><li><svg width="10" height="10" viewBox="0 0 10 10" fill="none" stroke="#8ea30e"><circle cx="5" cy="5" r="4.3"/><path d="m3 5 1.5 1.5L7 4"/></svg>Project Calculators</li><li><svg width="10" height="10" viewBox="0 0 10 10" fill="none" stroke="#8ea30e"><circle cx="5" cy="5" r="4.3"/><path d="m3 5 1.5 1.5L7 4"/></svg>Video Library</li></ul></div>
  <div class="foot-col abs" style="left:611px"><h4>For The <span class="accent">Pros</span></h4>
    <ul><li><svg width="10" height="10" viewBox="0 0 10 10" fill="none" stroke="#8ea30e"><circle cx="5" cy="5" r="4.3"/><path d="m3 5 1.5 1.5L7 4"/></svg>Trade Pro Program</li><li><svg width="10" height="10" viewBox="0 0 10 10" fill="none" stroke="#8ea30e"><circle cx="5" cy="5" r="4.3"/><path d="m3 5 1.5 1.5L7 4"/></svg>Trade Pro of the Month</li><li><svg width="10" height="10" viewBox="0 0 10 10" fill="none" stroke="#8ea30e"><circle cx="5" cy="5" r="4.3"/><path d="m3 5 1.5 1.5L7 4"/></svg>Trade Life</li></ul></div>
  <div class="badge abs" style="top:47px;height:75px"><span class="shape" style="width:130px;height:40px;background:#dfe3e8"></span></div>
  <div class="badge abs" style="top:131px;height:74px"><span class="shape" style="width:130px;height:46px;background:#1e5a8a"></span></div>
  <div class="foot-bottom abs">
    <span>© 2023 <span class="accent">Kestral</span>. All Rights Reserved.</span>
    <span style="margin-left:72px">Terms And Conditions &nbsp;&nbsp;|&nbsp;&nbsp; Privacy Policy</span>
    <span class="social"><span><i></i></span><span><i></i></span><span><i></i></span><span><i></i></span></span>
    <svg style="margin-left:auto" width="10" height="16" viewBox="0 0 10 16" fill="none" stroke="#8ea30e" stroke-width="1.3"><path d="M5 15V1M1 5l4-4 4 4"/></svg>
  </div>
</footer>

</body>
</html>
```